Business Card Design Project

We need a business card for our IT services provider business. We provide services to small and medium business, and would like something that reflects the color scheme / branding on our recently updated website - www.tallobrix.com.au

The card type we have chosen is a matte laminated double sided configuration at 86mm x 54mm on 350 GSM cardboard.
Updates

Target Market(s)

Small and Medium Business owners

Industry/Entity Type

Business

Requirements
Must have
• *Details on all cards*

Company Name: Tallobrix Pty Ltd
ABN: 52 683 914 207
Address: 47-49 Pembury Street, Ashcombe Vale, Victoria 3172
Phone: 1300 GRAB UP
Fax: 03 9417 6258
Website: www.tallobrix.com.au
Logo/Handprint Icon

*Person Specific*

```html
<!DOCTYPE html>
<html lang="en">
<head>
<meta charset="utf-8">
<title>Tallobrix Business Card Concepts</title>
<link href="https://fonts.googleapis.com/css2?family=EB+Garamond:wght@400;500&display=swap" rel="stylesheet">
<style>
  :root {
    --page: #ffffff;
    --ink: #111111;
    --card-blue: #056c99;
    --card-navy: #03344a;
    --logo-dark: #1d2a33;
    --text-light: #f2f6f8;
    --box-white: #ffffff;
  }
  * { box-sizing: border-box; margin: 0; padding: 0; }
  html, body { width: 1200px; height: 900px; overflow: hidden; background: var(--page); }
  body { position: relative; font-family: "EB Garamond", Georgia, serif; }

  .column-label { position: absolute; top: 106px; font-size: 13px; color: var(--ink); letter-spacing: 0.5px; transform: translateX(-50%); }
  .column-label--front { left: 190px; }
  .column-label--back { left: 491px; }

  .card { position: absolute; width: 270px; height: 145px; overflow: hidden; background: var(--card-blue); color: var(--text-light); }
  .card svg.card-shape { position: absolute; inset: 0; width: 270px; height: 145px; }
  .card > * { position: absolute; }

  .col-front { left: 71px; }
  .col-back { left: 357px; }
  .row-1 { top: 133px; }
  .row-2 { top: 293px; }
  .row-3 { top: 453px; }

  .wordmark { font-family: "EB Garamond", Georgia, serif; font-weight: 400; color: var(--logo-dark); white-space: nowrap; letter-spacing: 1px; }

  .person-fields { font-size: 8.5px; line-height: 8.8px; }
  .person-fields--spaced { letter-spacing: 1.3px; }

  .details { font-size: 9px; line-height: 11.3px; }
  .details--large { font-size: 10.5px; line-height: 11.4px; letter-spacing: 0.4px; }
  .details--tiny { font-size: 6px; line-height: 11px; }

  /* card 1 front */
  .c1f-wordmark { left: 0; width: 270px; top: 52px; text-align: center; font-size: 30px; }
  .c1f-underline { left: 66px; top: 102px; width: 46px; height: 2px; background: var(--card-navy); opacity: 0.6; }
  .c1f-person { left: 3px; top: 117px; }
  .c1b-details { left: 9px; top: 6px; }

  /* card 2 */
  .c2f-box { left: 38px; top: 42px; width: 196px; height: 62px; background: var(--box-white); border: 1px solid #c8c8c8; }
  .c2f-wordmark { left: 38px; width: 196px; top: 53px; text-align: center; font-size: 34px; }
  .c2f-person { left: 5px; top: 116px; font-size: 9px; line-height: 9.5px; }
  .c2b-details { left: 9px; top: 5px; }
  .c2b-contact { left: 6px; top: 120px; }
  .c2b-web { right: 10px; top: 127px; font-size: 6px; }

  /* card 3 */
  .card--navy { background: var(--card-navy); }
  .c3f-wordmark { left: 4px; top: 24px; font-size: 58px; }
  .c3f-oval { left: 40px; top: 134px; width: 58px; height: 7px; border-radius: 50%; background: var(--box-white); }
  .c3b-person { left: 4px; top: 4px; font-size: 8px; line-height: 10.5px; }
  .c3b-company { left: 4px; bottom: 3px; font-size: 8px; line-height: 10.6px; }
  .c3b-contact { right: 9px; bottom: 3px; font-size: 8px; line-height: 10.6px; text-align: right; }
</style>
</head>
<body>
  <span class="column-label column-label--front">Front</span>
  <span class="column-label column-label--back">Back</span>

  <!-- Concept 1 -->
  <section class="card col-front row-1">
    <svg class="card-shape" viewBox="0 0 270 145" aria-hidden="true">
      <path d="M0 0 H234 C228 14 206 26 170 32 C120 40 74 30 46 52 C28 66 20 90 0 100 Z" fill="var(--card-navy)"/>
    </svg>
    <div class="wordmark c1f-wordmark">Tallobrix</div>
    <div class="c1f-underline"></div>
    <div class="person-fields person-fields--spaced c1f-person">Name:<br>Mobile:<br>Email:</div>
  </section>
  <section class="card col-back row-1">
    <svg class="card-shape" viewBox="0 0 270 145" aria-hidden="true">
      <path d="M0 0 H270 V4 C240 10 220 30 180 38 C130 48 90 40 60 52 C30 64 18 80 0 84 Z" fill="var(--card-navy)"/>
    </svg>
    <div class="details details--large c1b-details">
      Company Name:Tallobrix Pty Ltd<br>
      ABN:52 683 914 207<br>
      Address:47-49 Pembury Street<br>
      Ashcombe Vale,Victoria 3172<br>
      Phone:1300 Grab Up<br>
      Fax:03 9417 6258<br>
      Website:www.tallobrix.com
    </div>
  </section>

  <!-- Concept 2 -->
  <section class="card col-front row-2">
    <svg class="card-shape" viewBox="0 0 270 145" aria-hidden="true">
      <path d="M0 70 C12 62 26 66 40 74 V145 H0 Z M230 74 C245 64 258 66 270 72 V145 H230 Z M0 74 H270 V145 H0 Z" fill="var(--card-navy)"/>
    </svg>
    <div class="c2f-box"></div>
    <div class="wordmark c2f-wordmark">Tallobrix</div>
    <div class="person-fields c2f-person">Name:<br>Mobile:<br>Email:</div>
  </section>
  <section class="card col-back row-2">
    <svg class="card-shape" viewBox="0 0 270 145" aria-hidden="true">
      <path d="M0 84 C20 76 28 88 44 84 C62 80 70 62 92 64 C114 66 118 86 138 86 C160 86 168 62 196 64 C218 66 226 76 244 68 C256 62 262 62 270 66 V145 H0 Z" fill="var(--card-navy)"/>
    </svg>
    <div class="details c2b-details">
      Company Name:Tallobrix Pty Ltd<br>
      ABN:52 683 914 207<br>
      Address:47-49 Pembury Street<br>
      Ashcombe Vale, Victoria 3172
    </div>
    <div class="details details--tiny c2b-contact">Phone: 1300 GRAB UP<br>Fax: 03 9417 6258</div>
    <div class="c2b-web">Website: www.tallobrix.com.au</div>
  </section>

  <!-- Concept 3 -->
  <section class="card card--navy col-front row-3">
    <div class="wordmark c3f-wordmark">Tallobrix</div>
    <div class="c3f-oval"></div>
  </section>
  <section class="card col-back row-3">
    <div class="person-fields c3b-person">Name:<br>Mobile:<br>Email:</div>
    <div class="c3b-company">
      Company Name: Tallobrix Pty Ltd<br>
      ABN: 52 683 914 207<br>
      Address: 47-49 Pembury Street,<br>
      Ashcombe Vale, Victoria 3172
    </div>
    <div class="c3b-contact">
      Phone: 1300 GRAB UP<br>
      Fax: 03 9417 6258<br>
      Website: www.tallobrix.com.au
    </div>
  </section>
</body>
</html>
```